Corliss Homes Website for luxury custom home builder with endless detail

Modern website for luxury custom home builder. Simple and easy for viewers to understand what we do. New company formed by retired custom home builder. Company concept is to simplify the building experience with modern technology and introduce a simple pricing strategy for the client. Website must flow. Prefer page less design or possibly something that is up and coming within the web design community. Two galleries: INTERIOR and EXTERIOR. I would like two click on box's when the website is opened showing the galleries as a centerpiece and would also prefer them to play as a slide show. The page needs to fit the entire screen in size. We would like to use Grey, Black and White or the shade of blue that is in our company logo. I would like to see one of my uploaded photos to be in the background. I would also like a 3rd box that will play some type of animated video describing what we do and what our process is. Hoping this would be more interactive for the viewer than clicking on buttons and navigating around wasting time.

Target Market(s)

affluent buyers ages 30-60 who want to built anything from large estates to downsized luzury homes for the retired crowd.

Industry/Entity Type

Home Builder

Number of Pages Required

1 page

Font styles to use
Sans Serif

Colors
33a6d7
000000
333333
5c5c5c
9d9d9d
d9d9d9

Requirements
Must have
• Logo and name at top of page. I would like a pageless web design that includes two gallery box's (Interior and Exterior photos) side by side on the first page. I would also like a 3rd box that will be a eVideo explaining what we do and how we do it. I want as little text as possible. I would like the background to be of one of my interior photos that will flow best and pop when the page loads.

```html
<!DOCTYPE html>
<html lang="en">
<head>
<meta charset="utf-8">
<title>Corliss Homes</title>
<link rel="stylesheet" href="https://fonts.googleapis.com/css2?family=Open+Sans:wght@400;600;700&display=swap">
<style>
:root{
  --blue:#33a6d7;
  --black:#000000;
  --ink:#333333;
  --mid:#5c5c5c;
  --soft:#9d9d9d;
  --pale:#d9d9d9;
  --white:#ffffff;
  --dark-band:#1e1e1e;
}
*{box-sizing:border-box;margin:0;padding:0}
html,body{width:1200px;height:2788px;overflow:hidden;background:var(--white)}
body{font-family:"Open Sans",Arial,sans-serif;color:var(--ink);position:relative}

/* hero */
.hero{position:absolute;left:0;top:0;width:1200px;height:660px;
  background:linear-gradient(180deg,#d8cbbd 0%,#efe7dc 35%,#e6d8c6 65%,#b9a48c 100%)}
.hero-photo{position:absolute;inset:0}
.nav{position:absolute;left:160px;top:0;width:880px;height:86px;background:rgba(60,50,45,.55);
  display:flex;justify-content:center}
.nav a{display:block;height:86px;line-height:86px;padding:0 26px;color:var(--white);
  font-size:15px;font-weight:600;text-decoration:none;letter-spacing:.5px}
.nav a.active{background:var(--black)}
.brand{position:absolute;left:0;width:1200px;top:270px;text-align:center}
.brand-square{display:inline-block;width:86px;height:86px;border:5px solid var(--ink);background:rgba(255,255,255,.55)}
.brand-name{margin-top:12px;font-size:40px;font-weight:600;color:var(--ink);letter-spacing:2px;text-transform:uppercase}
.hero-arrow{position:absolute;top:334px;width:34px;height:34px;border-radius:50%;background:rgba(40,40,40,.7)}
.hero-arrow.left{left:22px}.hero-arrow.right{right:22px}
.dots{position:absolute;top:604px;left:0;width:1200px;text-align:center}
.dots span{display:inline-block;width:8px;height:8px;border-radius:50%;background:var(--white);margin:0 10px;opacity:.6}
.dots span.on{opacity:1}

/* welcome */
.welcome{position:absolute;top:660px;left:0;width:1200px;text-align:center}
h2{font-size:40px;font-weight:400;letter-spacing:1px;text-transform:uppercase;color:var(--ink)}
h2 em{font-style:normal;color:var(--blue)}
.welcome h2{margin-top:40px}
.welcome p{width:820px;margin:26px auto 0;font-size:15px;line-height:24px;color:var(--mid)}
.btn-outline{display:inline-block;margin-top:52px;width:178px;height:56px;line-height:52px;border:2px solid var(--blue);
  color:var(--blue);font-size:15px;font-weight:600;text-transform:uppercase}
.rule{position:absolute;left:80px;width:1040px;height:1px;background:var(--pale)}

/* gallery */
.gallery{position:absolute;top:1030px;left:0;width:1200px;text-align:center}
.gallery .sub{margin-top:14px;font-size:13px;color:var(--soft)}
.tabs{position:relative;margin:30px auto 0;width:1050px;height:36px;border-bottom:2px solid var(--pale)}
.tabs span{display:inline-block;margin:0 34px;font-size:16px;color:var(--mid);text-transform:uppercase;line-height:30px}
.tabs span.on{color:var(--blue);border-bottom:2px solid var(--blue)}
.stage{position:absolute;left:75px;top:1212px;width:1050px;height:420px;
  background:linear-gradient(135deg,#c9c2b6 0%,#8c8272 40%,#6b6456 65%,#a9a495 100%)}
.stage-arrow{position:absolute;top:190px;width:0;height:0;border-top:14px solid transparent;border-bottom:14px solid transparent}
.stage-arrow.left{left:8px;border-right:14px solid var(--white)}
.stage-arrow.right{right:8px;border-left:14px solid var(--white)}
.thumbs{position:absolute;left:75px;top:1632px;width:1050px;height:172px;display:flex}
.thumbs div{flex:1;border-right:2px solid var(--white)}
.thumbs div:last-child{border-right:0}
.t1{background:#2c3035}.t2{background:linear-gradient(#b4a393,#6f5d4e)}.t3{background:linear-gradient(#d9d3cb,#8e8579)}
.t4{background:linear-gradient(#c7a26f,#6d4f2e)}.t5{background:linear-gradient(#e0a24f,#7b4d22)}.t6{background:linear-gradient(#a99479,#4f3d2c)}
.t1 svg{margin-top:66px}

/* what we do */
.services{position:absolute;top:1858px;left:0;width:1200px;height:222px;
  background:linear-gradient(180deg,#2a2a2a,#151515);text-align:center}
.services h2{color:var(--white);padding-top:40px}
.services p{width:480px;margin:14px auto 0;font-size:12px;line-height:18px;color:var(--pale)}
.cards{position:absolute;top:2082px;left:75px;width:1050px;height:240px;display:flex;gap:22px}
.card{flex:1;position:relative;border:3px solid var(--pale)}
.c1{background:linear-gradient(#9fd4ea,#5db7dd)}.c2{background:linear-gradient(#3d7f9c,#1d4a62)}.c3{background:linear-gradient(#8cb6d6,#5a6f7d)}
.card svg{position:absolute;left:50%;top:50%;margin:-28px 0 0 -28px}
.card .step{position:absolute;left:56px;bottom:18px;font-size:22px;font-weight:700;color:var(--ink)}

/* contact */
.contact{position:absolute;top:2370px;left:0;width:1200px;text-align:center}
.contact .sub{margin-top:10px;font-size:13px;color:var(--mid)}
.form{position:absolute;left:75px;top:2502px;width:640px;height:160px}
.field{position:absolute;background:var(--soft);color:var(--pale);font-size:12px;padding:8px 12px}
.f-name{left:0;top:0;width:310px;height:40px}
.f-mail{left:325px;top:0;width:310px;height:40px}
.f-msg{left:0;top:56px;width:420px;height:104px}
.send{position:absolute;left:434px;top:56px;width:206px;height:104px;background:var(--blue);color:var(--white);
  font-size:16px;text-align:center;padding-top:60px}
.info{position:absolute;left:830px;top:2500px;width:300px;font-size:13px;line-height:18px;color:var(--mid)}
.info li{list-style:none;position:relative;padding-left:34px;margin-bottom:12px}
.info svg{position:absolute;left:0;top:2px}
.social{margin-top:6px;display:flex;gap:6px;padding-left:34px}
.social span{width:28px;height:28px;background:var(--blue)}
.social span:first-child{background:#3b5a98}

/* footer */
.footer{position:absolute;left:0;top:2742px;width:1200px;height:46px;background:var(--black);
  color:var(--soft);font-size:12px;text-align:center;line-height:46px}
.footer b{color:var(--blue);font-weight:400}
.up{position:absolute;left:574px;top:2722px;width:52px;height:22px;background:var(--black);border-radius:26px 26px 0 0}
.up svg{position:absolute;left:18px;top:6px}
</style>
</head>
<body>

<header class="hero">
  <div class="hero-photo" role="img" aria-label="Sunlit luxury living room with timber-beamed ceiling, arched windows and fireplace"></div>
  <nav class="nav">
    <a class="active">HOME</a><a>ABOUT US</a><a>GALLERY</a><a>SERVICES</a><a>CONTACT US</a>
  </nav>
  <div class="brand">
    <span class="brand-square"></span>
    <div class="brand-name">Corliss Homes</div>
  </div>
  <svg class="hero-arrow left" viewBox="0 0 34 34"><path d="M20 11l-6 6 6 6" stroke="#fff" stroke-width="2.5" fill="none"/></svg>
  <svg class="hero-arrow right" viewBox="0 0 34 34"><path d="M14 11l6 6-6 6" stroke="#fff" stroke-width="2.5" fill="none"/></svg>
  <div class="dots"><span class="on"></span><span></span><span></span></div>
</header>

<section class="welcome">
  <h2>Welcom to <em>Corliss Homes</em></h2>
  <p>Lorem ipsum dolor sit amet, consectetur adipisicing elit, sed do eiusmod tempor incididunt ut labore et dolore magna aliqua. Ut enim ad minim veniam, quis nostrud exercitation ullamco laboris nisi ut aliquip ex ea commodo consequat. Duis aute irure dolor in reprehenderit in voluptate velit esse cillum dolore eu fugiat nulla pariatur. Excepteur sint occaecat cupidatat non proident.</p>
  <span class="btn-outline">Read more</span>
</section>
<div class="rule" style="top:1014px"></div>

<section class="gallery">
  <h2>Ouer <em>Gallery</em></h2>
  <p class="sub">Lorem ipsum dolor sit amet, consectetur adipisicing elit, sed do eiusmod tempor incididunt ut.</p>
  <div class="tabs"><span class="on">Interior</span><span>Exterior</span></div>
</section>
<div class="stage" role="img" aria-label="Covered patio with wicker lounge seating, round fire table and garden beyond">
  <span class="stage-arrow left"></span><span class="stage-arrow right"></span>
</div>
<div class="thumbs">
  <div class="t1"><svg width="40" height="40" viewBox="0 0 40 40"><circle cx="17" cy="17" r="9" stroke="#fff" stroke-width="3" fill="none"/><path d="M24 24l9 9" stroke="#fff" stroke-width="3"/></svg></div>
  <div class="t2" role="img" aria-label="Curved staircase in entry hall"></div>
  <div class="t3" role="img" aria-label="Bright white kitchen"></div>
  <div class="t4" role="img" aria-label="Wine cellar with wooden racks"></div>
  <div class="t5" role="img" aria-label="Warmly lit open kitchen"></div>
  <div class="t6" role="img" aria-label="Dining room with chandelier"></div>
</div>

<section class="services" role="img" aria-label="Dark-toned roofline of a finished home behind the heading">
  <h2>What <em>We Do</em></h2>
  <p>Ut enim ad minim veniam, quis nostrud exercitation ullamco laboris nisi ut aliquip ex ea commodo consequat.</p>
</section>
<div class="cards">
  <div class="card c1" role="img" aria-label="Animated explainer video, step one of the building process">
    <svg width="56" height="56" viewBox="0 0 56 56"><circle cx="28" cy="28" r="26" fill="none" stroke="#fff" stroke-width="3"/><path d="M22 17l17 11-17 11z" fill="#fff"/></svg>
    <span class="step">Step- 1</span>
  </div>
  <div class="card c2" role="img" aria-label="Video of a 3D home model with pool">
    <svg width="56" height="56" viewBox="0 0 56 56"><circle cx="28" cy="28" r="26" fill="none" stroke="#fff" stroke-width="3"/><path d="M22 17l17 11-17 11z" fill="#fff"/></svg>
  </div>
  <div class="card c3" role="img" aria-label="Video of a finished home exterior at dusk">
    <svg width="56" height="56" viewBox="0 0 56 56"><circle cx="28" cy="28" r="26" fill="none" stroke="#fff" stroke-width="3"/><path d="M22 17l17 11-17 11z" fill="#fff"/></svg>
  </div>
</div>

<section class="contact">
  <h2>Keep in <em>Touch</em></h2>
  <p class="sub">Get in Touch with CORLISS HOMES</p>
</section>
<div class="form">
  <div class="field f-name">Name</div>
  <div class="field f-mail">Email Id</div>
  <div class="field f-msg">Message</div>
  <div class="send">Send</div>
</div>
<ul class="info">
  <li><svg width="16" height="20" viewBox="0 0 16 20"><path d="M8 1a6 6 0 0 1 6 6c0 5-6 12-6 12S2 12 2 7a6 6 0 0 1 6-6z" fill="#5c5c5c"/><circle cx="8" cy="7" r="2" fill="#fff"/></svg>Lorem ipsum dolor sit amet, consectetur adipiscing elit, sed do.</li>
  <li><svg width="16" height="16" viewBox="0 0 16 16"><path d="M3 1l3 3-2 2c1 2 3 4 5 5l2-2 3 3-2 3C6 15 1 10 1 3z" fill="#5c5c5c"/></svg>+1 (555) 014-2290</li>
  <li><svg width="16" height="12" viewBox="0 0 16 12"><rect x="0.5" y="0.5" width="15" height="11" fill="none" stroke="#5c5c5c"/><path d="M1 1l7 6 7-6" stroke="#5c5c5c" fill="none"/></svg>mail@corlisshomes.example</li>
  <div class="social"><span></span><span></span></div>
</ul>

<div class="up"><svg width="16" height="10" viewBox="0 0 16 10"><path d="M2 8l6-6 6 6" stroke="#fff" stroke-width="2" fill="none"/></svg></div>
<footer class="footer">© <b>CORLISS HOMES</b> - 2015. all rights reserved.</footer>

</body>
</html>
```